Business card design needed

the business is HR Consulting, but its for SME businesses who cant afford a permanent HR person. We sell an HR info system to help them meet minimum employment legislation but with this hope they then require us on a monthly subscription to phone or email us for HR advice. We are HR qualified mums working from home

So we will be partners to HR and Payroll systems known as unify HR and Tally

Target Market(s)

Small to medium businesses so not black and overly corporate, but having said that many are accounting businesses

Industry/Entity Type

Business

Contact Information for Business Card

Name of the company: Maple HR

Me:Marta Oldenbrook
Title:Managing Director

m: 0438 615 209
e: marta@maplehr.com.au
w: www.maplehr.com.au

What we do: HR Consulting, HR Systems and support, Payroll Advice

Requirements
Nice to have
• there is a company already out there known as Harbor professionals. I like the leaves at the end as I wanted something different like this to the usual business logos but still professional. I wanted a symbol to show calm, positive, ease flow going up ,etc. but realise they have the leaves and possibly cant copy, or can we?..( kite??, something calm and positive)dont know!!. Green and blue needed to be in it as nature and calm as well. I love the colours of www.staffingfundco.com ( attached the colours), as well as the calm wave line underneath. have a look as while they use green and blue I loved the purple colour thrown in there.Green and blue on their own are so overused. I want vibrant. I want double sided and when on a table I want it to stand out so maybe the purple colour (as per the colours on the fund website) solid on one side with just the 3 services we provide and personal and company name on front but need some creativity from you guys.

```html
<!DOCTYPE html>
<html lang="en">
<head>
<meta charset="utf-8">
<title>Maple HR – Business Cards</title>
<link href="https://fonts.googleapis.com/css2?family=Ubuntu:wght@300;400&display=swap" rel="stylesheet">
<style>
  :root {
    --page-bg: #ecebe8;
    --teal-dark: #157f80;
    --teal-mid: #2a9d9c;
    --teal-light: #46b4b1;
    --magenta: #b32c9e;
    --magenta-mid: #cf6fc0;
    --pale: #efedef;
    --white: #ffffff;
    --white-soft: rgba(255,255,255,0.85);
  }
  * { box-sizing: border-box; margin: 0; padding: 0; }
  html, body {
    width: 1200px; height: 801px; overflow: hidden;
    background: var(--page-bg);
    font-family: "Ubuntu", sans-serif;
  }
  .canvas {
    position: relative; width: 1200px; height: 801px;
  }
  .card {
    position: absolute; top: 245px;
    width: 510px; height: 311px;
    border-radius: 4px;
    box-shadow: 0 6px 18px rgba(0,0,0,0.18);
    overflow: hidden;
    color: var(--white);
  }
  /* Front */
  .card--front {
    left: 60px;
    background: linear-gradient(135deg, var(--teal-light) 0%, var(--teal-mid) 45%, var(--teal-dark) 100%);
  }
  .brand {
    position: absolute; left: 40px; top: 40px;
    display: flex; align-items: center; gap: 10px;
    font-weight: 300; font-size: 20px; letter-spacing: 0.5px;
  }
  .brand__dot {
    width: 14px; height: 14px; border-radius: 50%;
    background: var(--white);
  }
  .person {
    position: absolute; left: 40px; top: 118px;
  }
  .person__name { font-weight: 300; font-size: 30px; line-height: 1.1; }
  .person__title { font-weight: 300; font-size: 15px; margin-top: 4px; color: var(--white-soft); }
  .contact {
    position: absolute; left: 40px; top: 196px;
    list-style: none; font-weight: 300; font-size: 13px; color: var(--white-soft);
  }
  .contact li { display: flex; align-items: center; gap: 9px; height: 21px; }
  .contact svg { width: 13px; height: 13px; flex: none; }
  .contact .no-icon { padding-left: 22px; }
  .services-line {
    position: absolute; left: 40px; bottom: 18px;
    font-weight: 300; font-size: 10px; color: var(--white-soft);
  }
  /* Back */
  .card--back {
    left: 630px;
    background: linear-gradient(210deg, var(--pale) 0%, #e6d6e3 30%, var(--magenta-mid) 62%, var(--magenta) 100%);
  }
  .back__content {
    position: absolute; left: 42px; top: 132px;
  }
  .back__name { font-weight: 300; font-size: 38px; line-height: 1.1; }
  .back__services { font-weight: 300; font-size: 13px; margin-top: 8px; color: var(--white-soft); }
</style>
</head>
<body>
<main class="canvas">
  <section class="card card--front" aria-label="Business card front">
    <div class="brand"><span class="brand__dot"></span><span>Maple HR</span></div>
    <div class="person">
      <h1 class="person__name">Marta Oldenbrook</h1>
      <p class="person__title">Managing Director</p>
    </div>
    <ul class="contact">
      <li>
        <svg viewBox="0 0 16 16" aria-hidden="true"><path fill="#fff" d="M4 1.5l2.2 3-1.3 1.6a8 8 0 0 0 5 5l1.6-1.3 3 2.2-1.2 2.3C8 14.5 1.5 8 1.7 2.7z"/></svg>
        <span>0438 615 209</span>
      </li>
      <li>
        <svg viewBox="0 0 16 16" aria-hidden="true"><rect x="1" y="3" width="14" height="10" rx="1" fill="none" stroke="#fff" stroke-width="1.4"/><path d="M1.5 4l6.5 5 6.5-5" fill="none" stroke="#fff" stroke-width="1.4"/></svg>
        <span>marta@maplehr.com.au</span>
      </li>
      <li class="no-icon"><span>www.maplehr.com.au</span></li>
    </ul>
    <p class="services-line">HR Consulting, HR Systems and Support, Payroll Advice</p>
  </section>

  <section class="card card--back" aria-label="Business card back">
    <div class="back__content">
      <h2 class="back__name">Marta Oldenbrook</h2>
      <p class="back__services">HR Consulting, HR Systems and Support, Payroll Advice</p>
    </div>
  </section>
</main>
</body>
</html>
```